Daybreak Ledger Booklet

I have a 25 page booklet that I wrote.
I need to have a book cover design, typesetting, and imagery.
I need it to be designed with bleeds because I am having it printed.
It will be in an 8.5 X 11 format.
Please look at the 2020*.png files for an idea for the cover.
The title of the mini-book is "Daybreak Ledger" .
Subtitle is "Crestlo Method for Health and Fitness Motivation"
Then in between the title and subtitle, place the "Tobin_Health_Infographic...." image.
The other images are for inside the mini-book,
The "Daybreak-Ledger-CrestlO.pdf" file is the information in the book that will need to be typesetted.
The other images are inside the book and will need to be placed inside when appropriate.
Please don't agree to do this project if you have not done this before
I also want to see your portfolio.
Thank you
P.S. I can add all my images that are in the booklet when you accept project

Target Market(s)

Baby boomers ages 50-70

Industry/Entity Type

Fitness

Colors
0a5aa6

Requirements
Must have
• My project consists of a book cover and back. And typesetting and imagery inside the book.

```html
<!DOCTYPE html>
<html lang="en">
<head>
<meta charset="utf-8">
<title>Daybreak Ledger – Booklet Cover</title>
<link rel="stylesheet" href="https://fonts.googleapis.com/css2?family=Bebas+Neue&family=Caprasimo&display=swap">
<style>
  :root {
    --stage: #e4e4e4;
    --navy: #10295e;
    --navy-deep: #031b4e;
    --navy-light: #2c4a80;
    --teal-title: #72c4b8;
    --white: #ffffff;
    --subtitle: #e6e7ea;
    --art-orange: #ee8a6e;
    --art-green: #45a83c;
    --art-teal: #66b7ae;
  }
  * { box-sizing: border-box; margin: 0; padding: 0; }
  html, body { width: 1200px; height: 800px; overflow: hidden; }
  body { background: var(--stage); position: relative; }

  .booklet-spread {
    position: absolute; left: 75px; top: 60px;
    width: 1050px; height: 680px; display: flex;
    box-shadow: 0 10px 30px rgba(0,0,0,0.25);
  }
  .cover { position: relative; width: 525px; height: 680px; overflow: hidden; }
  .cover--back {
    background: linear-gradient(100deg, var(--navy) 0%, var(--navy-light) 45%, var(--navy-deep) 75%, var(--navy) 100%);
  }
  .cover--front {
    background: linear-gradient(100deg, var(--navy-deep) 0%, var(--navy) 40%, var(--navy-deep) 70%, var(--navy) 100%);
  }

  .cover-title { font-weight: 400; }
  .title { position: absolute; font-family: "Caprasimo", serif; line-height: 1; font-size: 84px; white-space: nowrap; }
  .title__first { left: 60px; top: 115px; color: var(--teal-title); }
  .title__second { left: 120px; top: 205px; color: var(--white); }

  .stretching-infographic {
    position: absolute; left: 40px; top: 320px;
    width: 470px; height: 250px;
    border-radius: 40px;
    background: linear-gradient(120deg, var(--art-orange) 0%, var(--art-green) 50%, var(--art-teal) 100%);
  }

  .subtitle {
    position: absolute; left: 28px; top: 585px;
    font-family: "Bebas Neue", sans-serif; font-size: 40px; line-height: 1.02;
    color: var(--subtitle); letter-spacing: 0.5px; white-space: nowrap;
  }
</style>
</head>
<body>
  <div class="booklet-spread">
    <section class="cover cover--back" aria-label="Back cover"></section>

    <section class="cover cover--front" aria-label="Front cover">
      <h1 class="cover-title">
        <span class="title title__first">Daybreak</span>
        <span class="title title__second">Ledger</span>
      </h1>

      <div class="stretching-infographic" role="img"
           aria-label="Health infographic: speech-bubble illustration of dynamic, isometric and passive stretching"></div>

      <p class="subtitle">Crestlo Method for Health<br>and Fitness Motivation</p>
    </section>
  </div>
</body>
</html>
```